Our companies name is The Gilded Ladle and we specialize in craft cupcakes, what I mean by that is that we bake our cupcakes with craft beer and other alcoholic drinks. We are trying to focus on being elegant but at the same time unpretentious. Since we are incorporating beer in our cupcakes we want the business card to have our logo in the front and our information in the back.

Once we select the best design we will provide the contact information to be added. Thank you.

Industry/Entity Type

Business

Font styles to use
Decorative
Script

Requirements
Must have
• Round corners
Should not have
• Square corners

```html
<!DOCTYPE html>
<html lang="en">
<head>
<meta charset="utf-8">
<title>The Gilded Ladle — Business Card</title>
<link href="https://fonts.googleapis.com/css2?family=Lobster&family=Dancing+Script:wght@500&family=Cormorant+Garamond:wght@500&display=swap" rel="stylesheet">
<style>
  :root {
    --backdrop: #ece7e1;
    --card-white: #ffffff;
    --card-black: #050505;
    --name-red: #d81f2c;
    --ink: #1b1b1b;
    --mint: #86d3c8;
    --badge-red: #e3283a;
  }
  html, body {
    margin: 0;
    width: 1200px;
    height: 800px;
    overflow: hidden;
    background: var(--backdrop);
  }
  .canvas {
    position: relative;
    width: 1200px;
    height: 800px;
    display: flex;
    align-items: center;
    justify-content: center;
    gap: 80px;
  }
  .card {
    width: 340px;
    height: 595px;
    border-radius: 28px;
    box-shadow: 0 10px 30px rgba(0,0,0,0.18);
    position: relative;
    overflow: hidden;
  }
  .card-back {
    background: var(--card-white);
    text-align: center;
  }
  .card-front {
    background: var(--card-black);
    display: flex;
    align-items: center;
    justify-content: center;
  }
  .holder-name {
    position: absolute;
    top: 198px;
    left: 0;
    right: 0;
    margin: 0;
    font-family: "Lobster", cursive;
    font-weight: 400;
    font-size: 40px;
    color: var(--name-red);
  }
  .contact-phone {
    position: absolute;
    top: 282px;
    left: 0;
    right: 0;
    margin: 0;
    font-family: "Cormorant Garamond", serif;
    font-weight: 500;
    font-size: 27px;
    letter-spacing: 0.5px;
    color: var(--ink);
  }
  .contact-email {
    position: absolute;
    top: 320px;
    left: 0;
    right: 0;
    margin: 0;
    font-family: "Dancing Script", cursive;
    font-weight: 500;
    font-size: 23px;
    color: var(--ink);
  }
  .social-handle {
    position: absolute;
    top: 470px;
    left: 0;
    right: 0;
    margin: 0;
    font-family: "Dancing Script", cursive;
    font-weight: 500;
    font-size: 20px;
    color: var(--ink);
  }
  .brand-mark {
    display: flex;
    flex-direction: column;
    align-items: center;
    gap: 18px;
  }
  .brand-dot {
    width: 150px;
    height: 150px;
    border-radius: 50%;
    border: 4px solid var(--badge-red);
    box-sizing: border-box;
  }
  .brand-name {
    margin: 0;
    font-family: "Dancing Script", cursive;
    font-weight: 500;
    font-size: 44px;
    line-height: 1;
    color: var(--mint);
    white-space: nowrap;
  }
</style>
</head>
<body>
  <main class="canvas">
    <section class="card card-back" aria-label="Card back with contact details">
      <h1 class="holder-name">Rosa Delgado</h1>
      <p class="contact-phone">555-208-4417</p>
      <p class="contact-email">thegildedladle@inbox.com</p>
      <p class="social-handle">@gildedladle</p>
    </section>
    <section class="card card-front" aria-label="Card front with company name">
      <div class="brand-mark">
        <div class="brand-dot"></div>
        <p class="brand-name">The Gilded Ladle</p>
      </div>
    </section>
  </main>
</body>
</html>
```